Packaging design for HOT NEW RETAIL BEARD OIL BRAND - Merrow Dalton Apothecary

Packaging design for beard oils. I've attached a brief, and I've also attached a few examples of bottles and boxes. Of course, we need an entirely unique look. I've attached the photo of Merrow Dalton as well - you can choose to use it or not (I'm open).

This product will be sold at national retailers and needs to look like a brand that is sold at boutique

What the consumer wants to see on the shelf:
-Box should larger than others and be soft touch (feels luxurious)
-More “hipster look/feel”
-Text should stand out like inspiration photos - jumping off the shelf to the consumer
-Use the existing logo of Merrow Dalton
-Deco will be wrap label as shown in current product image
-Sample text to pull copy for outer carton (taken from label on glass bottle):
-Strengthen and condition your beard with this blend of natural oils. Sunflower oil is rich in omega, fatty acids and vitamins E, C, B, and A, while avocado oil hydrates the beard fibers from root to tip, keep the beard looking and feeling extraordinary. Smooth into your beard for a healthy sheen and a woodsy scent evoking the great outdoors.
-Cool/Hipster product at discount pricing

Target Market(s)

Men from ages 20-40. Women also buy this product for their men, so it needs to look like a well known brand.

Industry/Entity Type

Hair And Beauty

Font styles to use
Sans Serif

Colors

Designer to choose colors to be used in the design.

Requirements
Must have
• A full label and box design with key call outs:
• Features and benefits - found in attached brief
• Description of what it is: Beard Oil
• Name of frangrance: Sandalwood
• Size: 2 oz / 60 ml
Nice to have
• Feel free to revamp the logo if needed. I am not married to the font for Merrow Dalton Apothecary.

```html
<!DOCTYPE html>
<html lang="en">
<head>
<meta charset="utf-8">
<title>Merrow Dalton Apothecary – Sandalwood Beard Oil Packaging</title>
<link rel="stylesheet" href="https://fonts.googleapis.com/css2?family=Montserrat:wght@500;700;800&display=swap">
<style>
  :root {
    --bg: #f1f1f1;
    --navy: #4b4b6f;
    --navy-deep: #3a3a58;
    --ink: #0b0b0d;
    --paper: #f4f4f2;
  }
  * { margin: 0; padding: 0; box-sizing: border-box; }
  html, body { width: 1200px; height: 1116px; overflow: hidden; background: var(--bg); }
  .canvas {
    position: relative; width: 1200px; height: 1116px;
    font-family: "Montserrat", Arial, sans-serif; font-weight: 800;
    color: var(--paper); text-align: center;
  }
  .dashes { letter-spacing: 10px; line-height: 1; font-weight: 700; }

  /* Bottle wrap label */
  .label {
    position: absolute; left: 130px; top: 330px; width: 360px; height: 500px;
    background: var(--navy); overflow: hidden;
  }
  .label-portrait {
    position: absolute; left: 40px; top: 30px; width: 280px; height: 440px;
    background: var(--navy-deep); border-radius: 120px 120px 90px 90px; opacity: .8;
  }
  .label-text { position: relative; padding-top: 46px; }
  .label .brand-name { font-size: 29px; line-height: 1.02; letter-spacing: .5px; }
  .label .brand-sub {
    display: inline-block; font-size: 12px; font-weight: 700; letter-spacing: 1.5px;
    margin-top: 6px; padding: 4px 0;
    border-top: 2px solid var(--paper); border-bottom: 2px solid var(--paper);
  }
  .label .product { font-size: 42px; line-height: 1; margin-top: 30px; }
  .label .product small { display: block; font-size: 29px; margin-top: 2px; }
  .label .dashes { margin-top: 16px; font-size: 14px; }
  .label .scent { font-size: 18px; line-height: 1.1; margin: 8px 0; }
  .label .size { font-size: 14px; font-weight: 700; margin-top: 14px; }
  .label .benefit { font-size: 10px; font-weight: 500; letter-spacing: .5px; margin-top: 8px; }

  /* Box front panel */
  .box {
    position: absolute; left: 640px; top: 150px; width: 430px; height: 820px;
    overflow: hidden;
  }
  .box-shapes { position: absolute; inset: 0; }
  .box-text { position: absolute; inset: 0; }
  .box .word-beard {
    position: absolute; top: 30px; left: 0; right: 0;
    font-size: 84px; line-height: 90px; color: var(--navy); letter-spacing: -1px;
  }
  .box .word-oil { position: absolute; top: 130px; left: 0; right: 0; font-size: 80px; line-height: 1; }
  .box .dashes.top { position: absolute; top: 262px; left: 0; right: 0; font-size: 22px; letter-spacing: 14px; }
  .box .scent { position: absolute; top: 298px; left: 0; right: 0; font-size: 40px; line-height: 1.08; }
  .box .dashes.bottom { position: absolute; top: 446px; left: 0; right: 0; font-size: 22px; letter-spacing: 14px; }
  .box .size { position: absolute; top: 486px; left: 0; right: 0; font-size: 21px; }
  .box .benefits {
    position: absolute; top: 528px; left: 40px; right: 40px;
    font-size: 13px; font-weight: 500; line-height: 1.45;
  }
  .box .brand { position: absolute; right: 36px; bottom: 40px; width: 250px; }
  .box .brand-name { font-size: 36px; line-height: 1.02; }
  .box .brand-sub {
    display: inline-block; font-size: 16px; font-weight: 700; letter-spacing: 2px;
    margin-top: 8px; padding: 5px 0;
    border-top: 2px solid var(--paper); border-bottom: 2px solid var(--paper);
  }
</style>
</head>
<body>
<main class="canvas">

  <section class="label">
    <div class="label-portrait" role="img" aria-label="Illustrated bearded man portrait in dark navy tones"></div>
    <div class="label-text">
      <p class="brand-name">MERROW<br>DALTON</p>
      <p class="brand-sub">APOTHECARY</p>
      <h2 class="product">BEARD<small>OIL</small></h2>
      <p class="dashes">------</p>
      <p class="scent">SAND<br>AL<br>WOOD</p>
      <p class="dashes">------</p>
      <p class="size">2 fl oz / 60 ml</p>
      <p class="benefit">Strengthens &amp; conditions</p>
    </div>
  </section>

  <section class="box">
    <svg class="box-shapes" width="430" height="820" viewBox="0 0 430 820">
      <rect width="430" height="820" fill="var(--navy)"/>
      <rect x="0" y="30" width="430" height="90" fill="var(--ink)"/>
      <path role="img" aria-label="Large illustrated bearded man portrait in muted navy tones"
            d="M20 150 Q200 110 380 170 L380 640 Q200 760 20 660 Z" fill="var(--navy-deep)" opacity=".55"/>
      <polygon points="0,820 430,475 430,820" fill="var(--ink)"/>
    </svg>
    <div class="box-text">
      <h1 class="word-beard">BEARD</h1>
      <p class="word-oil">OIL</p>
      <p class="dashes top">-------</p>
      <p class="scent">SAND<br>AL<br>WOOD</p>
      <p class="dashes bottom">-------</p>
      <p class="size">2 fl oz / 60 ml</p>
      <p class="benefits">Sunflower oil rich in vitamins E, C, B &amp; A.<br>Avocado oil hydrates root to tip.<br>Healthy sheen, woodsy scent.</p>
      <div class="brand">
        <p class="brand-name">MERROW<br>DALTON</p>
        <p class="brand-sub">APOTHECARY</p>
      </div>
    </div>
  </section>

</main>
</body>
</html>
```